KVR GUARDING WEBSITE BANNER DESIGN OF AWESOME

Please take a look at the attached Banner. I want a redesign Idea. The requirements are below.

1)Must Use Website Background
2)Must Use Photo Provided
3)Must Include Button
4)Website the banner will be used on you can see the current at the bottom of the page: https://b.pelmarox.com

Target Market(s)

Anyone Seeking Security Guard Services

```html
<!DOCTYPE html>
<html lang="en">
<head>
<meta charset="utf-8">
<title>KVR Guarding – Website Banner</title>
<link href="https://fonts.googleapis.com/css2?family=Poppins:wght@400;500;700;800&display=swap" rel="stylesheet">
<style>
  :root {
    --board: #6f6f6f;
    --navy-top: #1b4c7c;
    --navy-band: #1a3560;
    --navy-base: #184672;
    --navy-deep: #163f6b;
    --gold: #f3ab1c;
    --gold-arc: #eaa920;
    --white: #ffffff;
    --photo-light: #4f7fb4;
    --photo-dark: #0f2745;
  }
  html, body {
    margin: 0;
    width: 1200px;
    height: 759px;
    overflow: hidden;
    background: var(--board);
    font-family: "Poppins", sans-serif;
  }
  .banner {
    position: absolute;
    left: 107px;
    width: 987px;
    height: 274px;
    overflow: hidden;
    background: var(--navy-base);
    box-shadow: 0 14px 40px rgba(0,0,0,0.45);
  }
  .banner--oval { top: 87px; }
  .banner--arcs { top: 398px; }
  .banner__art {
    position: absolute;
    inset: 0;
    width: 987px;
    height: 274px;
  }
  .banner__title {
    position: absolute;
    left: 36px;
    top: 18px;
    margin: 0;
    font-weight: 800;
    font-size: 38px;
    letter-spacing: -0.3px;
    color: var(--white);
  }
  .banner__tagline {
    position: absolute;
    left: 36px;
    top: 110px;
    margin: 0;
    font-weight: 500;
    font-size: 22px;
    color: var(--white);
  }
  .features {
    position: absolute;
    left: 36px;
    top: 162px;
    margin: 0;
    padding: 0;
    list-style: none;
    display: flex;
    gap: 11px;
    font-size: 13px;
    color: var(--white);
  }
  .features__item {
    display: flex;
    align-items: center;
    gap: 6px;
  }
  .features__item::before {
    content: "";
    width: 12px;
    height: 12px;
    border-radius: 50%;
    background: var(--gold);
  }
  .cta {
    position: absolute;
    left: 36px;
    top: 202px;
    width: 141px;
    height: 43px;
    border-radius: 22px;
    background: var(--gold);
    color: var(--navy-band);
    font-weight: 700;
    font-size: 13px;
    display: flex;
    align-items: center;
    justify-content: center;
    text-decoration: none;
  }
</style>
</head>
<body>

<section class="banner banner--oval">
  <svg class="banner__art" viewBox="0 0 987 274" aria-hidden="false">
    <defs>
      <radialGradient id="photoOval" cx="0.65" cy="0.3" r="0.8">
        <stop offset="0" stop-color="var(--photo-light)"/>
        <stop offset="1" stop-color="var(--photo-dark)"/>
      </radialGradient>
    </defs>
    <rect width="987" height="83" fill="var(--navy-top)"/>
    <polygon points="0,83 987,83 987,170 240,200 0,150" fill="var(--navy-band)"/>
    <rect x="780" width="207" height="274" fill="var(--navy-deep)"/>
    <circle cx="985" cy="137" r="198" fill="none" stroke="var(--gold-arc)" stroke-width="34"/>
    <circle cx="1096" cy="137" r="198" fill="none" stroke="var(--gold-arc)" stroke-width="34"/>
    <ellipse cx="677" cy="137" rx="173" ry="130" fill="var(--navy-base)" stroke="var(--gold)" stroke-width="9"/>
    <ellipse cx="677" cy="137" rx="146" ry="110" fill="url(#photoOval)" stroke="var(--gold)" stroke-width="5"
             role="img" aria-label="Photo of a security guard shining a flashlight up a dark stairwell"/>
  </svg>
  <h1 class="banner__title">Get Secured Today</h1>
  <p class="banner__tagline">We take your security personal.</p>
  <ul class="features">
    <li class="features__item">Client Portal</li>
    <li class="features__item">24x7 Dispatch</li>
    <li class="features__item">No Binding Contracts</li>
  </ul>
  <a class="cta" href="https://b.pelmarox.com">GET STARTED</a>
</section>

<section class="banner banner--arcs">
  <svg class="banner__art" viewBox="0 0 987 274">
    <defs>
      <radialGradient id="photoArc" cx="0.75" cy="0.25" r="0.85">
        <stop offset="0" stop-color="var(--photo-light)"/>
        <stop offset="1" stop-color="var(--photo-dark)"/>
      </radialGradient>
    </defs>
    <rect width="987" height="83" fill="var(--navy-top)"/>
    <polygon points="0,83 987,83 987,170 240,200 0,150" fill="var(--navy-band)"/>
    <circle cx="662" cy="137" r="206" fill="var(--navy-deep)" stroke="var(--gold-arc)" stroke-width="34"/>
    <circle cx="762" cy="137" r="190" fill="url(#photoArc)"
            role="img" aria-label="Photo of a security guard shining a flashlight up a dark stairwell"/>
    <circle cx="768" cy="137" r="202" fill="none" stroke="var(--gold-arc)" stroke-width="34"
            clip-path="inset(0 50% 0 0)"/>
    <circle cx="757" cy="137" r="204" fill="none" stroke="var(--gold-arc)" stroke-width="34"
            clip-path="inset(0 0 0 50%)"/>
  </svg>
  <h1 class="banner__title">Get Secured Today</h1>
  <p class="banner__tagline">We take your security personal.</p>
  <ul class="features">
    <li class="features__item">Client Portal</li>
    <li class="features__item">24x7 Dispatch</li>
    <li class="features__item">No Binding Contracts</li>
  </ul>
  <a class="cta" href="https://b.pelmarox.com">GET STARTED</a>
</section>

</body>
</html>
```